Re-branding for Structural Engineering firm

We need new business cards as part of our current re-branding. We have a new logo (attached), so the card design should incorporate this color scheme. We are a structural engineering firm providing structural building design and seismic consulting services. The final design should communicate professionalism and stability, with a modern look and feel.

```html
<!DOCTYPE html>
<html lang="en">
<head>
<meta charset="utf-8">
<title>Bravik Engineering – Business Card</title>
<link rel="stylesheet" href="https://fonts.googleapis.com/css2?family=Open+Sans:wght@400;600&display=swap">
<style>
  :root {
    --brand-blue: #1b75bc;
    --brand-grey: #808285;
    --ink: #111111;
    --bg-light: #eef0f4;
    --bg-mid: #d6dae4;
    --tile-pale: #cfe6f7;
    --tile-sky: #00aeef;
    --tile-navy: #2350a0;
    --tile-silver: #c4c4c4;
    --tile-steel: #7d7e80;
  }
  * { margin: 0; padding: 0; box-sizing: border-box; }
  html, body { width: 1200px; height: 668px; overflow: hidden; background: #ffffff; }
  .card {
    position: relative;
    width: 1200px;
    height: 668px;
    overflow: hidden;
    background: linear-gradient(90deg, var(--bg-light) 0%, var(--bg-mid) 75%);
    font-family: "Open Sans", sans-serif;
    color: var(--ink);
  }
  .mosaic-field {
    position: absolute;
    left: 711px;
    top: 0;
    width: 489px;
    height: 668px;
    background: linear-gradient(90deg,
      rgba(207,230,247,0) 0%,
      var(--tile-pale) 14%,
      var(--tile-sky) 30%,
      var(--brand-blue) 40%,
      var(--tile-navy) 52%,
      var(--tile-silver) 64%,
      var(--tile-steel) 82%,
      #a9a9a9 100%);
  }
  .brand {
    position: absolute;
    left: 93px;
    top: 91px;
    display: flex;
    align-items: flex-start;
  }
  .brand-square {
    width: 137px;
    height: 137px;
    background: var(--brand-blue);
    flex: none;
  }
  .brand-text { margin-left: 17px; }
  .brand-name {
    color: var(--brand-blue);
    font-weight: 600;
    font-size: 35px;
    line-height: 34px;
    letter-spacing: 0.5px;
    text-transform: uppercase;
  }
  .brand-address {
    margin-top: 10px;
    color: var(--brand-grey);
    font-weight: 600;
    font-size: 16.5px;
    line-height: 21.5px;
  }
  .brand-address .divider { color: var(--brand-blue); padding: 0 6px; }
  .person { position: absolute; left: 93px; top: 277px; }
  .person-name {
    font-size: 28px;
    font-weight: 400;
    letter-spacing: 0.3px;
    text-transform: uppercase;
    line-height: 38px;
  }
  .person-rule {
    width: 302px;
    height: 5px;
    background: var(--brand-blue);
    margin-top: 5px;
  }
  .person-role {
    margin-top: 20px;
    font-size: 23px;
    line-height: 30px;
  }
  .contact-list { position: absolute; left: 93px; top: 395px; list-style: none; }
  .contact-item {
    display: flex;
    align-items: center;
    height: 44px;
    margin-bottom: 23px;
    font-size: 23px;
  }
  .contact-icon {
    width: 44px;
    height: 44px;
    background: var(--brand-blue);
    margin-right: 13px;
    flex: none;
  }
</style>
</head>
<body>
  <main class="card">
    <div class="mosaic-field" role="img" aria-label="Decorative mosaic of blue and grey square tiles"></div>

    <header class="brand">
      <div class="brand-square"></div>
      <div class="brand-text">
        <div class="brand-name">Bravik<br>Engineering</div>
        <address class="brand-address" style="font-style:normal">
          4410 Harbor Ridge Dr., Ste. 210<br>
          Oakmont, California 90412<br>
          555.302.7140<span class="divider">|</span>www.bravikeng.com
        </address>
      </div>
    </header>

    <section class="person">
      <h1 class="person-name">Marcus Ellery</h1>
      <div class="person-rule"></div>
      <p class="person-role">Creative Director</p>
    </section>

    <ul class="contact-list">
      <li class="contact-item"><span class="contact-icon"></span>+001 5550 172 846</li>
      <li class="contact-item"><span class="contact-icon"></span>m.ellery@bravikeng.com</li>
    </ul>
  </main>
</body>
</html>
```